I need a website built for my organization.
We are the world's largest network of music producers.
The website should be professional, sharp, and high quality., We need a website built for The Harbor Sound Guild. We are one of the World's largest association of music producers.
The site must be professional, sharp, and high quality., I need a website built for my organization.
The site must be professional, sharp, and high quality.
Somewhere in the top half of the site there should be a form for the user to fill out. The details of the form are as follows:
Title (large and bold): Contact Us or Submit Your Music
Fields to include (* = required): First Name*, Last Name*, Age, Zip Code, Email Address*, Daytime Phone, Evening Phone, Comments
Then, there will be a "submit" button to proceed to next step of form. Just below the "submit" button, should be the following verbiage: "After submitting, you will have the opportunity to upload demos of your music (optional) and provide other pertinent information about yourself, band, or group."
Target Market(s)
Music producers and aspiring musicians
Industry/Entity Type
Group
Colors
Designer to choose colors to be used in the design.
Look and feel
Each slider illustrates characteristics of the customer's brand and the style your logo design should communicate.

```html
<!DOCTYPE html>
<html lang="en">
<head>
<meta charset="UTF-8">
<title>The Harbor Sound Guild</title>
<link href="https://fonts.googleapis.com/css2?family=Gelasio:wght@700&family=Roboto:ital,wght@0,400;1,300&display=swap" rel="stylesheet">
<style>
  :root {
    --black: #000000;
    --panel: rgba(16, 16, 16, 0.9);
    --gold: #d4a02c;
    --gold-dark: #8a621c;
    --logo-box: #2a2a2a;
    --logo-text: #6e6e6e;
    --field: #ffffff;
    --field-text: #333333;
    --note: #f2f2f2;
    --footer-text: #8c8c8c;
    --icon: #6a6a6a;
  }
  * { box-sizing: border-box; margin: 0; padding: 0; }
  html, body { width: 1200px; height: 763px; overflow: hidden; background: var(--black); }
  body { position: relative; font-family: "Roboto", Arial, sans-serif; }

  .site-header { position: absolute; left: 0; top: 0; width: 1200px; height: 70px; background: var(--black); }
  .logo-slot {
    position: absolute; left: 507px; top: 15px; width: 188px; height: 42px;
    background: var(--logo-box); color: var(--logo-text);
    font: 700 13px/42px "Roboto", Arial, sans-serif; letter-spacing: 6px; text-align: center;
  }

  .hero { position: absolute; left: 0; top: 70px; width: 1200px; height: 656px; overflow: hidden; }
  .hero-photo {
    position: absolute; inset: 0;
    background:
      radial-gradient(ellipse 420px 360px at 1080px 420px, #d8d8d8 0%, rgba(180,180,180,0.6) 40%, rgba(0,0,0,0) 75%),
      linear-gradient(160deg, #b4b4b4 0%, #6c6c6c 40%, #2a2a2a 70%, #1a1a1a 100%);
  }
  .hero-photo::before {
    content: ""; position: absolute; left: 0; top: 0; width: 560px; height: 656px;
    background: radial-gradient(ellipse 330px 420px at 230px 330px, #0a0a0a 0%, #111 70%, rgba(17,17,17,0) 100%);
  }

  .signup-panel {
    position: absolute; left: 600px; top: 75px; width: 449px; height: 505px;
    background: var(--panel); border: 1px solid var(--gold-dark);
  }
  .signup-title {
    position: absolute; left: 0; top: 42px; width: 100%;
    font: 700 19.5px/27px "Gelasio", Georgia, serif; color: var(--gold); text-align: center;
  }
  .field {
    position: absolute; height: 30px; background: var(--field);
    font: italic 300 12px/30px "Roboto", Arial, sans-serif; color: var(--field-text); padding-left: 9px;
  }
  .field.half-left { left: 27px; width: 193px; }
  .field.half-right { left: 228px; width: 193px; }
  .field.full { left: 27px; width: 394px; }
  .field.comments { height: 61px; line-height: 30px; }
  .field .chevron { position: absolute; right: 8px; top: 11px; }

  .submit-button {
    position: absolute; left: 84px; top: 372px; width: 281px; height: 47px;
    border-radius: 6px; background: linear-gradient(#c99a3a, #7e5a1c);
    color: #ffffff; font: 700 15px/47px "Gelasio", Georgia, serif; text-align: center; letter-spacing: 0.2px;
  }
  .submit-button svg { vertical-align: -1px; margin-left: 6px; }
  .submit-note {
    position: absolute; left: 20px; top: 430px; width: 409px;
    font: 400 10.5px/15px "Roboto", Arial, sans-serif; color: var(--note); text-align: center;
  }

  .site-footer {
    position: absolute; left: 0; top: 726px; width: 1200px; height: 37px; background: var(--black);
    display: flex; justify-content: center; align-items: center; gap: 6px;
    font: 400 10.5px "Roboto", Arial, sans-serif; color: var(--footer-text);
  }
  .social-list { display: flex; gap: 5px; margin-left: 4px; }
  .social-dot { width: 18px; height: 18px; border-radius: 50%; background: var(--icon); }
</style>
</head>
<body>
  <header class="site-header">
    <div class="logo-slot">LOGO</div>
  </header>

  <main class="hero">
    <div class="hero-photo" role="img" aria-label="Black and white concert photo of a singer in silhouette at a microphone under stage lights"></div>

    <section class="signup-panel">
      <h1 class="signup-title">We are the world's largest network of<br>music producers.<br>Contact Us or Submit Your Music!</h1>

      <div class="field half-left" style="top:147px">First Name*</div>
      <div class="field half-right" style="top:147px">Last Name*</div>
      <div class="field half-left" style="top:185px">Age
        <svg class="chevron" width="12" height="8" viewBox="0 0 12 8"><path d="M1 1l5 5 5-5" fill="none" stroke="#bbbbbb" stroke-width="2.2"/></svg>
      </div>
      <div class="field half-right" style="top:185px">Zip Code</div>
      <div class="field full" style="top:222px">Email Address*</div>
      <div class="field half-left" style="top:260px">Daytime Phone</div>
      <div class="field half-right" style="top:260px">Evening Phone</div>
      <div class="field full comments" style="top:297px">Comments</div>

      <div class="submit-button">SUBMIT YOUR PROFILE
        <svg width="8" height="11" viewBox="0 0 8 11"><path d="M1.5 1l4.5 4.5-4.5 4.5" fill="none" stroke="#ffffff" stroke-width="2.4"/></svg>
      </div>
      <p class="submit-note">After submitting, you will have the opportunity to upload demos of your music (optional) and provide other pertinent information about yourself, band, or group.</p>
    </section>
  </main>

  <footer class="site-footer">
    <span>Terms of Use&nbsp;&nbsp;/&nbsp;&nbsp;©2013 The Harbor Sound Guild.</span>
    <div class="social-list">
      <span class="social-dot"></span>
      <span class="social-dot"></span>
      <span class="social-dot"></span>
      <span class="social-dot"></span>
    </div>
  </footer>
</body>
</html>
```